Plantwise Mechanics Partners. Needs a Business Card Design

We need a business card design for an engineering company which supplies industrial components (pumps, compressors, mechanical seals) provides repairs and services for above mentioned equipments. We offer a uniqe engineering solutions which help our customers to increase the productivness of their manufacturings, and energy savings.

Target Market(s)

Chemical and energy plants, refineries. Food industry and private consumers in a less.

Industry/Entity Type

Business

Contact Information for Business Card

Stylish and sleek design oriented on industrial area.

Requirements
Should not have
• company name shortening

```html
<!DOCTYPE html>
<html lang="en">
<head>
<meta charset="utf-8">
<title>Plantwise Mechanics Partners – Business Card</title>
<link rel="stylesheet" href="https://fonts.googleapis.com/css2?family=Open+Sans:wght@400;600;700&display=swap">
<style>
  :root {
    --backdrop: #3a3532;
    --card-black: #050505;
    --card-glow: #222222;
    --accent-red: #ee3a34;
    --accent-yellow: #fbab2f;
    --accent-blue: #1f3c9c;
    --text-white: #ffffff;
    --text-soft: #e8e8e8;
  }
  * { margin: 0; padding: 0; box-sizing: border-box; }
  html, body {
    width: 1200px; height: 844px; overflow: hidden;
    background: var(--backdrop);
    font-family: "Open Sans", Arial, sans-serif;
  }
  .canvas {
    position: relative; width: 1200px; height: 844px;
  }
  .card {
    position: absolute; top: 267px;
    width: 540px; height: 310px;
    background: var(--card-black);
    overflow: hidden;
    box-shadow: 0 10px 28px rgba(0,0,0,.45);
  }
  /* Back side: contact details */
  .card-back { left: 40px; }
  .card-back .band-top {
    position: absolute; left: 0; top: 0; width: 100%; height: 13px;
    background: var(--accent-red);
  }
  .card-back .band-bottom {
    position: absolute; left: 0; bottom: 0; width: 100%; height: 13px;
    background: var(--accent-yellow);
  }
  .identity {
    position: absolute; top: 64px; left: 0; width: 100%;
    text-align: center;
  }
  .person-name {
    display: inline-block;
    font-size: 15px; font-weight: 600; letter-spacing: .3px;
    padding: 0 6px 2px;
    border-bottom: 1px solid var(--accent-red);
  }
  .person-name .first { color: var(--accent-red); }
  .person-name .last { color: var(--accent-yellow); }
  .person-role {
    margin-top: 2px;
    font-size: 12px; color: var(--text-soft);
  }
  .contact-list {
    position: absolute; top: 150px; left: 0; width: 100%;
    list-style: none; text-align: center;
    font-size: 12.5px; line-height: 17px; color: var(--text-soft);
  }
  .address {
    position: absolute; top: 252px; left: 0; width: 100%;
    text-align: center;
    font-size: 13px; color: var(--text-white);
  }
  /* Front side: company name */
  .card-front {
    left: 620px;
    background: radial-gradient(ellipse at 55% 45%, var(--card-glow) 0%, var(--card-black) 62%);
  }
  .tab-left {
    position: absolute; left: 0; top: 118px; width: 38px; height: 38px;
    background: var(--accent-red);
    border-right: 4px solid var(--accent-blue);
  }
  .tab-right {
    position: absolute; right: 0; top: 30px; width: 34px; height: 34px;
    background: var(--accent-yellow);
    border-left: 4px solid var(--accent-blue);
  }
  .brand {
    position: absolute; left: 0; top: 112px; width: 100%;
    display: flex; flex-direction: column; align-items: center; gap: 18px;
  }
  .brand-dot {
    width: 44px; height: 44px; border-radius: 50%;
    background: var(--accent-red);
  }
  .brand-name {
    font-size: 27px; font-weight: 700; color: var(--text-white);
    letter-spacing: .2px;
  }
</style>
</head>
<body>
<main class="canvas">
  <section class="card card-back" aria-label="Business card, contact side">
    <div class="band-top"></div>
    <div class="identity">
      <p class="person-name"><span class="first">DANIEL</span> <span class="last">MERCER</span></p>
      <p class="person-role">Managing Director</p>
    </div>
    <ul class="contact-list">
      <li>044-318-2205</li>
      <li>123-640-7719</li>
      <li>office@plantwisepartners.com</li>
      <li>www.plantwisepartners.com</li>
    </ul>
    <p class="address">58 Foundry Row | Northvale, AB | 204817</p>
    <div class="band-bottom"></div>
  </section>

  <section class="card card-front" aria-label="Business card, company side">
    <div class="tab-right"></div>
    <div class="tab-left"></div>
    <div class="brand">
      <span class="brand-dot"></span>
      <p class="brand-name">Plantwise Mechanics Partners</p>
    </div>
  </section>
</main>
</body>
</html>
```